Baustellen-Schild / Plakat für das HausKT
Zielgruppe
Ich bin Privatmann und ich saniere ein Haus, mit hochwertigen Materialien regionaler Hersteller. Ich will ein Baustellen schild schön gestaltet haben, mit einer Visualisierung des Entwurfs wie das Haus einmal aussehen soll, als auch mit einigen Informationen. Das ganze soll eine markante, hochwertige Typographie erhalten und gut gesetzt sein. Gerne darf dazu illustriert werden um das ganze ansprechend, modern und ästhetisch zu gestalten.
Aufgabenstellung
Ein schönes Schild gestalten.
Moodboard für interiors und exterior des Hauses gibt es hier: https://www.pinnwalt.so/jorikbeland
Es wird ein schönes Haus :-)

```html
<!DOCTYPE html>
<html lang="de">
<head>
<meta charset="utf-8">
<title>HausKT – Baustellenschild</title>
<link rel="stylesheet" href="https://fonts.googleapis.com/css2?family=Open+Sans:wght@400;700&display=swap">
<style>
  :root {
    --brown: #4e2a1a;
    --ink: #111111;
    --paper: #ffffff;
    --wood-light: #d9c3a3;
    --wood-dark: #5e5040;
    --sky-dusk: #9d8aa6;
    --sky-day: #a9c1d3;
    --sketch: #ebe4cf;
    --kitchen: #c79a62;
  }
  * { margin: 0; padding: 0; box-sizing: border-box; }
  html, body { width: 1200px; height: 849px; overflow: hidden; background: var(--paper); }
  .sign {
    position: relative;
    width: 1200px;
    height: 849px;
    background: var(--paper);
    font-family: "Open Sans", "Segoe UI", sans-serif;
    color: var(--ink);
  }
  .band { position: absolute; left: 0; width: 1200px; background: var(--brown); }
  .band--top-1 { top: 11px; height: 12px; }
  .band--top-2 { top: 204px; height: 13px; }
  .band--bottom-1 { top: 634px; height: 11px; }
  .band--bottom-2 { top: 828px; height: 11px; }

  .gallery { position: absolute; left: 0; width: 1200px; display: flex; }
  .gallery--exterior { top: 28px; height: 172px; }
  .gallery--interior { top: 652px; height: 171px; }
  .gallery__tile { flex: 1 1 0; height: 100%; }

  .tile--house-light { background: linear-gradient(180deg, var(--sky-day) 0%, #d5cbbf 45%, #cdb99c 70%, #6f8a44 100%); }
  .tile--house-dusk { background: linear-gradient(180deg, var(--sky-dusk) 0%, #c9a48a 45%, #a88a6b 70%, #6c6a68 100%); }
  .tile--house-dark { background: linear-gradient(180deg, var(--sky-day) 0%, #6d6256 40%, #56493c 70%, #6f8d47 100%); }
  .tile--house-larch { background: linear-gradient(180deg, #c9d7df 0%, #d8bc97 40%, #cfae86 75%, #8aa560 100%); }
  .tile--kitchen-light { background: linear-gradient(180deg, #e9e8e6 0%, #e2c9a4 55%, var(--kitchen) 100%); }
  .tile--sketch-front { background: linear-gradient(180deg, #f2ebd3 0%, var(--sketch) 100%); }
  .tile--sketch-side { background: linear-gradient(180deg, #e4e0cf 0%, #ddd8c4 100%); }
  .tile--kitchen-oak { background: linear-gradient(180deg, #eeeeec 0%, #b98650 50%, #8e5c2e 100%); }

  .headline { position: absolute; left: 0; width: 1200px; text-align: center; }
  .headline__intro { top: 288px; font-weight: 400; font-size: 38px; line-height: 1; letter-spacing: 0.2px; }
  .headline__title { top: 340px; font-weight: 700; font-size: 126px; line-height: 1; color: var(--brown); letter-spacing: -1px; }
  .headline__tagline { top: 494px; font-weight: 700; font-size: 30px; line-height: 1; }

  .social { position: absolute; left: 1000px; top: 587px; display: flex; align-items: center; gap: 8px; }
  .social__dot { width: 34px; height: 34px; border-radius: 50%; background: var(--brown); }
  .social__handle { font-size: 21px; font-weight: 400; color: var(--ink); }
</style>
</head>
<body>
<main class="sign">
  <div class="band band--top-1"></div>
  <section class="gallery gallery--exterior">
    <div class="gallery__tile tile--house-light" role="img" aria-label="Foto: helles Holzhaus mit Satteldach auf einer Wiese"></div>
    <div class="gallery__tile tile--house-dusk" role="img" aria-label="Foto: Holzhaus mit Carport in der Abenddämmerung"></div>
    <div class="gallery__tile tile--house-dark" role="img" aria-label="Foto: dunkles Holzhaus mit beleuchteter Terrasse"></div>
    <div class="gallery__tile tile--house-larch" role="img" aria-label="Foto: Haus mit Lärchenholzfassade und Dachfenstern"></div>
  </section>
  <div class="band band--top-2"></div>

  <p class="headline headline__intro">Hier entsteht Ihr neues</p>
  <h1 class="headline headline__title">Traumhaus</h1>
  <p class="headline headline__tagline">modern · regional · hochwertig</p>

  <div class="social">
    <span class="social__dot"></span>
    <span class="social__handle">@haus_kt</span>
  </div>

  <div class="band band--bottom-1"></div>
  <section class="gallery gallery--interior">
    <div class="gallery__tile tile--kitchen-light" role="img" aria-label="Foto: Küchenmodul aus hellem Holz mit Spüle"></div>
    <div class="gallery__tile tile--sketch-front" role="img" aria-label="Skizze: Entwurf der Hausfront mit Bäumen"></div>
    <div class="gallery__tile tile--sketch-side" role="img" aria-label="Skizze: Entwurf der Hausansicht mit Holzverschalung"></div>
    <div class="gallery__tile tile--kitchen-oak" role="img" aria-label="Foto: Küchenmodul aus Eichenholz mit Regal"></div>
  </section>
  <div class="band band--bottom-2"></div>
</main>
</body>
</html>
```